Plume Ovenworks, need a business card design for an innovative bakery

This is a new company out of Boston. We develop innovative baking products. I would you to make a simple card with the colors attached. The design should be modern and fun. Our tag line is " The sweetest way to gift". This should be incorporated into the design.

Industry/Entity Type

Business

Contact Information for Business Card

Plume Ovenworks LLC

Font styles to use
Sans Serif

Requirements
Must have
• Felix Marrow
• Address: 818 Tindle Ave, Suite 2190, Newton MA, 02466
• Phone: 617-5930268
• Emial: FelixMarrow@plumeovenworks.example

```html
<!DOCTYPE html>
<html lang="en">
<head>
<meta charset="utf-8">
<title>Plume Ovenworks – Business Card</title>
<link rel="stylesheet" href="https://fonts.googleapis.com/css2?family=Arimo:wght@400;700&display=swap">
<style>
  :root {
    --stage: #3a3b3d;
    --card-navy: #16223a;
    --ribbon: #2ab3b8;
    --ribbon-light: #4fd0d2;
    --ribbon-dark: #168a90;
    --text-teal: #3fbfc0;
    --name-teal: #7fd6d3;
    --tagline: #ffffff;
    --brand: #c9ccd2;
  }
  * { margin: 0; padding: 0; box-sizing: border-box; }
  html, body {
    width: 1200px; height: 900px; overflow: hidden;
    background: var(--stage);
    font-family: "Arimo", Arial, sans-serif;
  }
  .business-card {
    position: absolute; left: 100px; top: 150px;
    width: 1000px; height: 600px;
    background: var(--card-navy);
    border-radius: 28px;
    overflow: hidden;
    box-shadow: 0 18px 40px rgba(0,0,0,0.45);
  }
  .ribbon-bands { position: absolute; inset: 0; }
  .bow {
    position: absolute; left: 90px; top: 70px;
    width: 330px; height: 250px;
    border-radius: 38px;
    background: linear-gradient(145deg, var(--ribbon-light) 0%, var(--ribbon) 50%, var(--ribbon-dark) 100%);
  }
  .brand {
    position: absolute; right: 60px; top: 120px;
    display: flex; align-items: center; gap: 14px;
  }
  .brand-mark {
    width: 20px; height: 20px; border-radius: 50%;
    background: var(--ribbon-light);
  }
  .brand-name {
    font-weight: 700; font-size: 42px; color: var(--brand);
    letter-spacing: 0.5px;
  }
  .tagline {
    position: absolute; right: 60px; top: 240px;
    font-weight: 700; font-size: 32px; line-height: 40px; color: var(--tagline);
  }
  .contact {
    position: absolute; right: 50px; top: 340px;
    text-align: right; color: var(--text-teal);
  }
  .contact-name {
    font-weight: 400; font-size: 36px; color: var(--name-teal);
    margin-bottom: 18px; margin-right: 40px;
  }
  .contact-list { list-style: none; }
  .contact-item {
    display: flex; justify-content: flex-end; align-items: center;
    gap: 16px; font-size: 24px; line-height: 40px;
  }
  .contact-icon { width: 24px; height: 24px; flex: none; }
</style>
</head>
<body>
  <article class="business-card">
    <svg class="ribbon-bands" width="1000" height="600" viewBox="0 0 1000 600" aria-hidden="true">
      <defs>
        <linearGradient id="band-shade" x1="0" y1="0" x2="0" y2="1">
          <stop offset="0" stop-color="#4fd0d2"/>
          <stop offset="0.5" stop-color="#2ab3b8"/>
          <stop offset="1" stop-color="#168a90"/>
        </linearGradient>
      </defs>
      <rect class="band-vertical" x="220" y="0" width="72" height="600" fill="#2ab3b8"/>
      <rect class="band-horizontal" x="0" y="220" width="1000" height="80" fill="url(#band-shade)"/>
    </svg>

    <div class="bow" role="img" aria-label="Satin teal ribbon bow tied where the bands cross"></div>

    <div class="brand">
      <span class="brand-mark"></span>
      <span class="brand-name">Plume Ovenworks</span>
    </div>

    <p class="tagline">The sweetest way to gift</p>

    <section class="contact">
      <h1 class="contact-name">Felix Marrow</h1>
      <ul class="contact-list">
        <li class="contact-item">617-5930268
          <svg class="contact-icon" viewBox="0 0 24 24" aria-hidden="true"><path fill="#fff" d="M6.6 2.5l3 3.4-1.8 2.3c1 2.3 3.6 5 6 6l2.3-1.8 3.4 3-2 3.2C11 19 5 13 3.4 4.5z"/></svg>
        </li>
        <li class="contact-item">FelixMarrow@plumeovenworks.example
          <svg class="contact-icon" viewBox="0 0 24 24" aria-hidden="true"><rect x="2.5" y="5.5" width="19" height="13" fill="none" stroke="#fff" stroke-width="1.6"/><path d="M2.5 5.5l9.5 7.5 9.5-7.5" fill="none" stroke="#fff" stroke-width="1.6"/></svg>
        </li>
        <li class="contact-item">www.plumeovenworks.example
          <svg class="contact-icon" viewBox="0 0 24 24" aria-hidden="true"><g fill="none" stroke="#fff" stroke-width="1.6"><circle cx="12" cy="12" r="9.5"/><ellipse cx="12" cy="12" rx="4.5" ry="9.5"/><path d="M2.5 12h19M4 7h16M4 17h16"/></g></svg>
        </li>
        <li class="contact-item">818 Tindle Ave, Suite 2190, Newton MA, 02466
          <svg class="contact-icon" viewBox="0 0 24 24" aria-hidden="true"><path fill="#fff" d="M12 2a7 7 0 0 0-7 7c0 5 7 13 7 13s7-8 7-13a7 7 0 0 0-7-7zm0 10a3 3 0 1 1 0-6 3 3 0 0 1 0 6z"/></svg>
        </li>
      </ul>
    </section>
  </article>
</body>
</html>
```